Have Logo - Need Business Card Design!!!

I am looking for a business card design for a real estate development business. The company name is Corvell Estate Group. I already have a logo created by Sketch Harbor and would like this logo to be incorporated into the design. I have uploaded the files. The card needs to be professional, but visually interesting. Not necessary to be double-sided, but if you want to get creative and can think of something to put on the back then have at it.

Target Market(s)

The target audience for these business cards will be professionals in the real estate industry.

Industry/Entity Type

Real Estate

Requirements
Must have
• The business card must have all the necessary items for a business card, i.e. company name, our logo, name (however, not title necessary), office address, office phone number, cell number, fax number, website address, etc.

You can use the information below for the card:

Gregory L. Hanlon
782 Marlowe Avenue
San Francisco, California 94127

www.corvellestategroup.example
ghanlon@corvellestategroup.example
Office: 415-555-0142
Fax: 415-555-0143
Cell: 415-555-0186

```html
<!DOCTYPE html>
<html lang="en">
<head>
<meta charset="utf-8">
<title>Corvell Estate Group – Business Card</title>
<link rel="stylesheet" href="https://fonts.googleapis.com/css2?family=Open+Sans:wght@600;700&family=Crimson+Text&display=swap">
<style>
  :root {
    --page: #e4e4e2;
    --card: #ffffff;
    --navy: #212a5c;
    --green: #007a3d;
    --grey: #4d4a48;
    --ink: #3a3a3a;
    --white: #ffffff;
  }
  * { margin: 0; padding: 0; box-sizing: border-box; }
  html, body { width: 1200px; height: 1199px; overflow: hidden; background: var(--page); }
  .stage { position: relative; width: 1200px; height: 1199px; }
  .card {
    position: absolute; left: 281px; width: 601px; height: 500px;
    background: var(--card); border-radius: 48px; overflow: hidden;
    box-shadow: 0 4px 14px rgba(0,0,0,0.18);
  }
  .card--front { top: 53px; }
  .card--back { top: 618px; }

  .company-name {
    position: absolute; font-family: "Open Sans", sans-serif; font-weight: 600;
    font-size: 32px; letter-spacing: 0.5px; white-space: nowrap; line-height: 1;
  }
  .card--front .company-name { left: 0; right: 0; top: 196px; text-align: center; color: var(--navy); }
  .card--back .company-name { right: 58px; top: 68px; color: var(--grey); }

  .front-band {
    position: absolute; left: 0; right: 0; top: 343px; bottom: 0; background: var(--navy);
    display: flex; align-items: center; justify-content: center; padding-top: 16px;
  }
  .website {
    font-family: "Open Sans", sans-serif; font-weight: 700; font-size: 19px;
    letter-spacing: 3px; color: var(--white); white-space: nowrap;
  }

  .name-band {
    position: absolute; left: 0; right: 0; top: 164px; height: 39px; background: var(--green);
    display: flex; align-items: center; justify-content: center;
  }
  .person-name {
    font-family: "Open Sans", sans-serif; font-weight: 700; font-size: 23px;
    letter-spacing: 0.5px; color: var(--white);
  }

  .details {
    font-family: "Crimson Text", serif; font-size: 17px; color: var(--ink); line-height: 1;
  }
  .address { position: absolute; left: 56px; top: 255px; }
  .address p { height: 28px; }
  .contact-row { display: flex; align-items: center; gap: 12px; position: absolute; }
  .contact-row svg { width: 20px; height: 20px; fill: var(--grey); flex: none; }
  .email { left: 56px; top: 325px; white-space: nowrap; }
  .phones { position: absolute; left: 412px; top: 255px; }
  .phones .contact-row { position: static; height: 35px; }
</style>
</head>
<body>
<main class="stage">
  <section class="card card--front" aria-label="Card front">
    <span class="company-name">Corvell Estate Group</span>
    <div class="front-band">
      <span class="website">www.corvellestategroup.example</span>
    </div>
  </section>

  <section class="card card--back" aria-label="Card back">
    <span class="company-name">Corvell Estate Group</span>
    <div class="name-band"><span class="person-name">Gregory L. Hanlon</span></div>

    <div class="details address">
      <p>782 Marlowe Avenue</p>
      <p>San Francisco, California 94127</p>
    </div>

    <div class="details contact-row email">
      <svg viewBox="0 0 20 20" aria-hidden="true"><path d="M2 8 L10 3 L18 8 V17 H2 Z M3.5 9 L10 13.5 L16.5 9 V15.5 H3.5 Z" fill-rule="evenodd"/></svg>
      <span>ghanlon@corvellestategroup.example</span>
    </div>

    <div class="details phones">
      <div class="contact-row">
        <svg viewBox="0 0 20 20" aria-hidden="true"><path d="M4 2 L7.5 1.5 L9 6 L7 7.5 C8 10 10 12 12.5 13 L14 11 L18.5 12.5 L18 16 C17.5 17.5 16 18.5 14 18 C8 16.5 3.5 12 2 6 C1.5 4 2.5 2.5 4 2 Z"/></svg>
        <span>415-555-0142</span>
      </div>
      <div class="contact-row">
        <svg viewBox="0 0 20 20" aria-hidden="true"><path d="M5 2 H14 V7 H18 V15 H15 V18 H5 V15 H2 V7 H5 Z M7 4 V7 H12 V4 Z M7 13 V16 H13 V13 Z" fill-rule="evenodd"/></svg>
        <span>415-555-0143</span>
      </div>
      <div class="contact-row">
        <svg viewBox="0 0 20 20" aria-hidden="true"><path d="M5 1 H15 V19 H5 Z M7 3 V8 H13 V3 Z M7 10 H9 V12 H7 Z M11 10 H13 V12 H11 Z M7 14 H9 V16 H7 Z M11 14 H13 V16 H11 Z" fill-rule="evenodd"/></svg>
        <span>415-555-0186</span>
      </div>
    </div>
  </section>
</main>
</body>
</html>
```